I would like a business card to match my truck wrap and logo. I would like the font to match my existing business card please.

Industry/Entity Type

Painter

Contact Information for Business Card

Rodrigo Venaza 801-437-2916 Venazacoatings.utah@brushmail.net
SERVICES - Custom Paint & Stain, Interior & Exterior, Epoxy Coatings / Garage Floors, Cabinet Refinishing, Log Staining and Refinishing.

Requirements
Nice to have
• I would like to have the white and grey line like the bottom of my vehicle wrap, Light Grey to match my truck also.

```html
<!DOCTYPE html>
<html lang="en">
<head>
<meta charset="utf-8">
<title>Venaza Painting – Business Card</title>
<link rel="stylesheet" href="https://fonts.googleapis.com/css2?family=Saira:ital,wght@0,700;1,700;1,800&family=Roboto:wght@400;700&display=swap">
<style>
  :root {
    --bg: #2a2b2d;
    --card-white: #ffffff;
    --card-dark: #1d1e20;
    --pattern-dark: #26272a;
    --brand-blue: #16a2e6;
    --brand-blue-deep: #0b6fb8;
    --rule-grey: #8a8a8a;
    --text-light: #f4f4f4;
  }
  html, body {
    margin: 0;
    width: 1200px;
    height: 1108px;
    overflow: hidden;
    background: var(--bg);
  }
  .stage {
    position: relative;
    width: 1200px;
    height: 1108px;
  }
  .card {
    position: absolute;
    top: 244px;
    width: 360px;
    height: 620px;
    border-radius: 18px;
    overflow: hidden;
    box-sizing: border-box;
  }
  /* Front */
  .card-front {
    left: 180px;
    background: var(--card-white);
    text-align: center;
  }
  .brand {
    position: absolute;
    top: 150px;
    left: 0;
    right: 0;
    display: flex;
    flex-direction: column;
    align-items: center;
    gap: 18px;
  }
  .brand-square {
    width: 56px;
    height: 56px;
    background: var(--brand-blue);
    border-radius: 6px;
  }
  .brand-name {
    font-family: "Saira", sans-serif;
    font-weight: 700;
    color: var(--brand-blue);
    font-size: 40px;
    line-height: 1.05;
    letter-spacing: 2px;
    text-transform: uppercase;
  }
  .contact {
    position: absolute;
    left: 0;
    right: 0;
    bottom: 56px;
    font-family: "Saira", sans-serif;
    font-style: italic;
    font-weight: 800;
    color: var(--brand-blue);
  }
  .contact-name {
    font-size: 27px;
    letter-spacing: 0.5px;
    text-transform: uppercase;
  }
  .contact-rule {
    width: 130px;
    height: 1px;
    margin: 10px auto 8px;
    background: var(--rule-grey);
  }
  .contact-phone {
    font-size: 24px;
    margin-bottom: 4px;
  }
  .contact-email {
    font-size: 16.5px;
    font-weight: 700;
  }
  /* Back */
  .card-back {
    left: 660px;
    background: var(--card-dark);
  }
  .back-pattern {
    position: absolute;
    inset: 0 0 200px 0;
    background: linear-gradient(160deg, var(--pattern-dark) 0%, var(--card-dark) 100%);
  }
  .back-brand {
    position: absolute;
    top: 300px;
    left: 0;
    right: 0;
    display: flex;
    flex-direction: column;
    align-items: center;
    gap: 8px;
  }
  .back-brand .brand-square {
    width: 40px;
    height: 40px;
    border-radius: 4px;
  }
  .back-brand .brand-name {
    font-size: 18px;
    letter-spacing: 1px;
  }
  .services {
    position: absolute;
    left: 0;
    right: 0;
    top: 405px;
    text-align: center;
    font-family: "Roboto", sans-serif;
    color: var(--text-light);
  }
  .services-title {
    font-weight: 700;
    font-size: 21px;
    margin: 0 0 4px;
  }
  .services-list {
    list-style: none;
    margin: 0;
    padding: 0;
    font-size: 19px;
    line-height: 1.45;
  }
</style>
</head>
<body>
<main class="stage">
  <section class="card card-front">
    <div class="brand">
      <span class="brand-square"></span>
      <span class="brand-name">Venaza<br>Painting</span>
    </div>
    <div class="contact">
      <div class="contact-name">Rodrigo Venaza</div>
      <div class="contact-rule"></div>
      <div class="contact-phone">801-437-2916</div>
      <div class="contact-email">Venazacoatings.utah@brushmail.net</div>
    </div>
  </section>

  <section class="card card-back">
    <div class="back-pattern" role="img" aria-label="Subtle tone-on-tone repeating brand pattern"></div>
    <div class="back-brand">
      <span class="brand-square"></span>
      <span class="brand-name">Venaza Painting</span>
    </div>
    <div class="services">
      <h2 class="services-title">SERVICES</h2>
      <ul class="services-list">
        <li>Custom Paint &amp; Stain</li>
        <li>Interior &amp; Exterior</li>
        <li>Epoxy Coatings / Garage Floors</li>
        <li>Cabinet Refinishing</li>
        <li>Log Staining and Refinishing.</li>
      </ul>
    </div>
  </section>
</main>
</body>
</html>
```